established lighting store -latest lighting designs

I would like a design for a 2 sided brochure (front and back) A4
I own a lighting store and have been servicing and supplying lights for 16 years
We supply lighting to over 100 builders
We work with designers ,architects, home renovators
We have the latest designs and trends in lighting
We offer personalised service to all our customers
We can help you with the lighting design of your new home or commercial project

We currently supply lights to about 20 builders who have display homes in a display village nearby http://dwellorbit.com.au
These display homes have potential buyers of the homes walking through them and therefore potential customers of ours.
Usually the builder will refer the client to us but it would be nice to have some kind of presence in the display home in the way of a brochure.
This will enable us to possibly pick up client who are just browsing thru the homes

I'd the photos to do most of the talking with a description similar to the brochure attached .(which says "at nexar lighting pembry vale we excel......) PLEASE NOTE COMPANY NAME IS NOW
NEXAR LIGHTING PEMBRY VALE

we will need
company name NEXAR LIGHTING PEMBRY VALE
logo ATTACHED
address UNIT 27 / 4 MARLOWE ST , PEMBRY VALE
phone no 97418305

and an invitation to come into our showroom with their plans to help them with their lighting layout and to help them select the right lighting for their home

i like the idea of black background with the photos overlaping with border around each
photos can be cropped to suit

some sample black background brochures attached

Target Market(s)

NEW HOME OWNERS BUILDING NEW HOMES NEEding lights
builders clients
renovators

Industry/Entity Type

Store

Font styles to use
Sans Serif

Colors
000000
5c5c5c
606060
fbed22
ec1f27
0255a3
00a990
9bcb3c
f37122

Requirements
Must have
• black background
• pictures to be the main focus
• short write up on our services and invitation to visit our store
Nice to have
• please note we are not
• nexar lighting pembry vale (as per some of the previous ads)
• we are now
• nexar light pembry vale
• ++++++++++++++++++++++++++++
• from some wording from our competitors websites
• """"""Quarrel Lighting is the newest and most distinctive destination for lighting in Sydney. We pride ourselves on sourcing both unique and accessible products with a range that will continue to evolve as new designs and options become available.
• Our service is personalised, and we aim to assist your design choices; be it feature lights in Willoughby, functional lights in Annandale, or an entire home lighting solution.
• Offering a fresh approach to interior and exterior designer lighting in Annandale and Willoughby, our display range includes distinct style European imports through to products that are sourced and manufactured locally. It is our intention to bring together a select range of high quality items to meet the discerning customer’s taste and practical requirements.""""""
• """"""""Here at Fennick Lighting, we have been creating light for over 40 years. Our professional staff, including interior designers and electrical engineers can creatively respond to aesthetic and functional issues with a clear focus on client satisfaction. We are a full-service lighting destination, offering expert advice in layout and design as well as comprehensive style guidance. We are authorised lighting partners with some of the world’s most prestigious and exclusive lighting manufacturers, showcased in our ever-evolving showroom."""
• """Responding to local trends as well as emerging European concepts, we offer an abundance of individual and creative possibilities with an extensive range of contemporary and traditional fittings. We specialise in everything from period restorations to cutting-edge modern and with thousands of stock items, inspiration is never far away. We are truly passionate about light. Come and see why we are different. Call or drop in today or take advantage of our appointment service at Australia’s premiere lighting destination.""""

```html
<!DOCTYPE html>
<html lang="en">
<head>
<meta charset="utf-8">
<title>Nexar Lighting Pembry Vale – Brochure</title>
<link href="https://fonts.googleapis.com/css2?family=Oswald:wght@500;600&family=Arimo:wght@400;700&family=Carlito:ital@1&display=swap" rel="stylesheet">
<style>
  :root{
    --black:#000000;
    --ink:#1b1c21;
    --ink-2:#2a2b31;
    --grey:#5c5c5c;
    --silver:#d9d9d9;
    --red:#ec1f27;
    --red-deep:#c8141b;
    --yellow:#fbed22;
    --yellow-deep:#f5c914;
    --white:#ffffff;
    --canvas:#e4e4e4;
  }
  *{box-sizing:border-box;margin:0;padding:0}
  html,body{width:1200px;height:1200px;overflow:hidden;background:var(--canvas)}
  .page{position:absolute;top:285px;width:480px;height:677px;overflow:hidden;
    background:linear-gradient(180deg,var(--ink-2),var(--ink) 60%,#121317);
    box-shadow:0 2px 6px rgba(0,0,0,.25)}
  .page--front{left:82px}
  .page--back{left:626px}
  .layer{position:absolute;left:0;top:0}
  .photo{position:absolute;border:4px solid var(--white);box-shadow:0 3px 5px rgba(0,0,0,.45)}
  .headline{position:absolute;font-family:"Oswald",sans-serif;font-weight:600;line-height:1.05;letter-spacing:-.2px}
  .headline .yellow{color:var(--yellow)}
  .headline .white{color:var(--white)}
  .contact{position:absolute;font-family:"Arimo",sans-serif;line-height:1}
  .contact__label{color:var(--red);font-weight:700}
  .contact__number{color:var(--black);display:block}
  .body-copy{position:absolute;font-family:"Carlito",sans-serif;font-style:italic;color:var(--white);text-align:justify}
  .body-copy p+p{margin-top:10px}
  .brand{position:absolute;display:flex;align-items:center;gap:6px;font-family:"Arimo",sans-serif;
    font-weight:400;font-size:11px;color:var(--white);letter-spacing:.5px}
  .brand__dot{width:7px;height:7px;background:var(--yellow)}
  .footer{position:absolute;left:0;bottom:0;width:480px;height:43px;background:var(--red);
    border-top:5px solid var(--silver);display:flex;align-items:center;justify-content:center;
    font-family:"Arimo",sans-serif;font-size:13.5px;color:var(--white);letter-spacing:3.2px}
  .hours{position:absolute;font-family:"Arimo",sans-serif;font-size:14px;line-height:17px;color:var(--black);text-align:right}
  .services{position:absolute;font-family:"Oswald",sans-serif;font-weight:500;text-align:right;color:var(--white);line-height:23px;font-size:18px}
  .services .lead{color:var(--yellow);font-weight:600;font-size:24px;line-height:30px}
  .services .bullet{color:var(--yellow);font-size:12px;margin-left:5px}
</style>
</head>
<body>

<!-- FRONT -->
<section class="page page--front">
  <svg class="layer" width="480" height="677" viewBox="0 0 480 677">
    <defs>
      <linearGradient id="silverBand" x1="0" y1="0" x2="0" y2="1">
        <stop offset="0" stop-color="#f2f2f2"/><stop offset="1" stop-color="#bdbdbd"/>
      </linearGradient>
      <linearGradient id="yellowBlock" x1="0" y1="0" x2="0" y2="1">
        <stop offset="0" stop-color="#fbed22"/><stop offset="1" stop-color="#f5c914"/>
      </linearGradient>
    </defs>
    <rect x="0" y="293" width="480" height="10" fill="url(#silverBand)"/>
    <polygon points="264,0 480,0 480,293 252,293 254,247 318,135" fill="var(--red)"/>
    <polygon points="320,151 480,151 480,224 282,224" fill="url(#silverBand)"/>
    <polygon points="267,303 480,303 480,551 283,551 267,535" fill="url(#yellowBlock)"/>
    <rect x="0" y="622" width="480" height="12" fill="var(--silver)"/>
  </svg>

  <svg class="layer" width="480" height="300" viewBox="0 0 480 300" role="img" aria-label="Modern two-storey home lit at dusk with a glass-fenced pool">
    <defs>
      <linearGradient id="heroFront" x1="0" y1="0" x2="0" y2="1">
        <stop offset="0" stop-color="#2c56b8"/><stop offset=".45" stop-color="#6f7fa8"/>
        <stop offset=".7" stop-color="#b8894a"/><stop offset="1" stop-color="#1c2a4a"/>
      </linearGradient>
    </defs>
    <polygon points="0,0 256,0 311,135 252,248 252,293 0,293" fill="url(#heroFront)"/>
    <polyline points="260,0 315,135 254,249" fill="none" stroke="var(--yellow)" stroke-width="8"/>
  </svg>

  <div class="services" style="right:16px;top:28px">
    <div class="lead">We work with</div>
    <div>Interior Designers<span class="bullet">●</span></div>
    <div>Architects<span class="bullet">●</span></div>
    <div>Home renovators<span class="bullet">●</span></div>
  </div>

  <div class="hours" style="right:23px;top:163px">Monday to Saturday<br>9am till 5pm<br>Sunday 10am till 4pm</div>

  <div class="photo" role="img" aria-label="Living room with blue lounge and soft cove lighting" style="left:32px;top:249px;width:126px;height:82px;background:linear-gradient(160deg,#d9c9a0,#4f86b8 55%,#24406a)"></div>
  <div class="photo" role="img" aria-label="Kitchen with linear pendant lights" style="left:182px;top:249px;width:125px;height:82px;background:linear-gradient(170deg,#eeeeee,#9a9a9a 50%,#6b4a34)"></div>
  <div class="photo" role="img" aria-label="Dining room with chandelier and garden view" style="left:325px;top:249px;width:125px;height:82px;background:linear-gradient(160deg,#e7e2d5,#7c8f58 45%,#5a3a2a)"></div>

  <h2 class="headline" style="left:30px;top:360px;font-size:30px">
    <span class="yellow">We supply lighting</span><br><span class="white">to over 100 builders</span>
  </h2>

  <div class="body-copy" style="left:30px;top:436px;width:224px;font-size:8.4px;line-height:10.6px">
    <p>Quarrel Lighting is the newest and most distinctive destination for lighting in Sydney. We pride ourselves on sourcing both unique and accessible products with a range that will continue to evolve as new designs and options become available.</p>
    <p>Our service is personalised, and we aim to assist your design choices; be it feature lights in Willoughby, functional lights in Annandale, or an entire home lighting solution.</p>
    <p>Offering a fresh approach to interior and exterior designer lighting in Annandale and Willoughby, our display range includes distinct style European imports through to products that are sourced and manufactured locally. It is our intention to bring together a select range of high quality items to meet the discerning customer’s taste and practical requirements.</p>
  </div>

  <div class="contact" style="left:288px;top:354px">
    <span class="contact__label" style="font-size:29px">Contact US</span>
    <span class="contact__number" style="font-size:37px;margin-top:3px">97418305</span>
  </div>

  <div class="photo" role="img" aria-label="Wall lights washing a stone facade at night" style="left:294px;top:433px;width:157px;height:97px;background:linear-gradient(120deg,#3a4a5e,#1e2735 45%,#b57a3c 65%,#dcd8d0)"></div>

  <div class="brand" style="left:294px;top:577px"><span class="brand__dot"></span>NEXAR Lighting</div>

  <footer class="footer">www.nexarlighting.com.au</footer>
</section>

<!-- BACK -->
<section class="page page--back">
  <svg class="layer" width="480" height="677" viewBox="0 0 480 677">
    <defs>
      <linearGradient id="silverBandB" x1="0" y1="0" x2="0" y2="1">
        <stop offset="0" stop-color="#f2f2f2"/><stop offset="1" stop-color="#bdbdbd"/>
      </linearGradient>
    </defs>
    <polygon points="0,0 220,0 154,257 0,257" fill="var(--red)"/>
    <polygon points="0,119 189,119 167,205 0,205" fill="url(#silverBandB)"/>
    <polygon points="0,252 150,270 480,178 480,202 150,290 0,268" fill="var(--yellow)"/>
    <rect x="0" y="622" width="480" height="12" fill="var(--silver)"/>
  </svg>

  <svg class="layer" width="480" height="260" viewBox="0 0 480 260" role="img" aria-label="White contemporary home at night with palm tree and uplit walls">
    <defs>
      <linearGradient id="heroBack" x1="0" y1="0" x2="1" y2="1">
        <stop offset="0" stop-color="#1f3fa0"/><stop offset=".45" stop-color="#c9d3e6"/>
        <stop offset=".75" stop-color="#3e5a2a"/><stop offset="1" stop-color="#1a2340"/>
      </linearGradient>
    </defs>
    <polygon points="220,0 480,0 480,180 154,256" fill="url(#heroBack)"/>
  </svg>

  <h2 class="headline" style="left:23px;top:26px;font-size:22px;line-height:23.5px">
    <span class="white">We have the latest</span><br><span class="yellow">designs and trends</span><br><span class="white">in lighting services</span>
  </h2>

  <div class="contact" style="left:23px;top:132px">
    <span class="contact__label" style="font-size:29px">Contact US</span>
    <span class="contact__number" style="font-size:36px;margin-top:2px">97418305</span>
  </div>

  <div class="brand" style="left:281px;top:270px"><span class="brand__dot"></span>NEXAR Lighting</div>

  <h2 class="headline" style="left:31px;top:308px;font-size:19px;line-height:25px">
    <span class="white">We work with designers ,architects, home renovators</span><br>
    <span class="yellow">We offer personalised service to all our customers</span>
  </h2>

  <div class="body-copy" style="left:31px;top:377px;width:420px;font-size:8.2px;line-height:10.6px">
    <p>Here at Fennick Lighting, we have been creating light for over 40 years. Our professional staff, including interior designers and electrical engineers can creatively respond to aesthetic and functional issues with a clear focus on client satisfaction. We are a full-service lighting destination, offering expert advice in layout and design as well as comprehensive style guidance. We are authorised lighting partners with some of the world’s most prestigious and exclusive lighting manufacturers, showcased in our ever-evolving showroom.</p>
    <p style="margin-top:11px">Responding to local trends as well as emerging European concepts, we offer an abundance of individual and creative possibilities with an extensive range of contemporary and traditional fittings. We specialise in everything from period restorations to cutting-edge modern and with thousands of stock items, inspiration is never far away. We are truly passionate about light. Come and see why we are different. Call or drop in today or take advantage of our appointment service at Australia’s premiere lighting destination.</p>
  </div>

  <div class="photo" role="img" aria-label="Spherical pendant light in a bright room" style="left:27px;top:515px;width:126px;height:83px;background:radial-gradient(circle at 45% 50%,#b89a5c 0,#6d6450 25%,#cfd2d4 60%,#9ea3a6)"></div>
  <div class="photo" role="img" aria-label="Garden plant uplit with warm light" style="left:176px;top:515px;width:127px;height:83px;background:radial-gradient(circle at 50% 45%,#e6e37a 0,#8a9a2a 30%,#2e3410 75%)"></div>
  <div class="photo" role="img" aria-label="Glowing spherical pendant casting patterned shadows" style="left:326px;top:515px;width:128px;height:83px;background:radial-gradient(circle at 52% 40%,#f0e0c8 0,#8a7d70 25%,#2b2b2e 70%)"></div>

  <footer class="footer">www.nexarlighting.com.au</footer>
</section>

</body>
</html>
```